Web Design Project

We need a web design new company based in Australia. We're a search engine marketing company who predominantly manages Vexora bidlines campaigns.
Currently still deciding on a business name so lets use “Marlow Tappers” for now.
Target market....
small to medium size businesses
- more clicks to their website from the 1st page of Vexora
- more relevant, (higher quality) clicks
- higher return on investment from their bidlines campaign
- more sales, leads, (conversions)
We'd like clean, simple, semi-professional as we'd like to pick up some high end corporate clients.
A website that we love the look and feel of – but they’re a direct competitor so can’t be too similar in design.
http://www.brindlepath.com.au/search-engine-marketing.html
**please check portfolio on this web page..they designs are absolutely stunning!! http://www.brindlepath.com.au/website-design.html
Updates
Please refer to the attached file, a rough sketch of my web page.
place replace...."Afraid your bidlines campaign is underperforming with,....
Industry/Entity Type
Business
Look and feel

```html
<!DOCTYPE html>
<html lang="en">
<head>
<meta charset="utf-8">
<title>Marlow Tappers – Search Engine Marketing</title>
<link href="https://fonts.googleapis.com/css2?family=Quicksand:wght@400;500;600&display=swap" rel="stylesheet">
<style>
  :root {
    --blue: #62a5d2;
    --brand-blue: #1a78c2;
    --ink: #5f5f5f;
    --ink-soft: #8a8a8a;
    --nav-active: #a9a9a9;
    --rule: #6fa8d6;
    --band: #c4c4c4;
    --white: #ffffff;
    --paper: #ffffff;
  }
  * { box-sizing: border-box; margin: 0; padding: 0; }
  html, body { width: 1029px; height: 1200px; overflow: hidden; background: var(--paper); }
  body { position: relative; font-family: "Quicksand", sans-serif; color: var(--ink); }

  .brand { position: absolute; left: 152px; top: 31px; display: flex; align-items: center; gap: 8px; }
  .brand-mark { width: 49px; height: 41px; background: var(--brand-blue); border-radius: 3px; }
  .brand-name { font-size: 25px; font-weight: 600; color: var(--ink); letter-spacing: 0.2px; }

  .phone { position: absolute; right: 150px; top: 66px; font-size: 19px; font-weight: 600; color: var(--ink); }
  .header-rule { position: absolute; left: 153px; top: 101px; width: 723px; height: 1px; background: var(--rule); }

  .main-nav { position: absolute; left: 150px; top: 126px; width: 728px; display: flex; justify-content: space-between; }
  .main-nav a { font-size: 21px; color: #3f3f3f; text-decoration: none; }
  .main-nav a.is-active { color: var(--nav-active); }

  .hero-badge { position: absolute; left: 193px; top: 247px; width: 252px; height: 252px; border-radius: 50%;
    background: var(--blue); color: var(--white); display: flex; align-items: center; justify-content: center;
    font-size: 60px; font-weight: 400; }
  .hero-title { position: absolute; left: 481px; top: 246px; width: 340px; font-size: 39px; font-weight: 400;
    line-height: 42px; color: var(--blue); }
  .hero-title .muted { color: var(--ink); }

  .health-check { position: absolute; left: 88px; top: 590px; width: 867px; height: 72px; background: var(--band); }
  .health-check h2 { position: absolute; left: 74px; top: 22px; font-size: 22px; font-weight: 400; color: var(--white); letter-spacing: 0.3px; }
  .health-check .url-field { position: absolute; left: 458px; top: 20px; width: 245px; height: 31px; background: var(--white);
    border: 1px solid #8c8c8c; font-family: Arial, sans-serif; font-size: 12px; color: #333; padding: 0 9px; line-height: 29px; }
  .health-check .next-link { position: absolute; left: 733px; top: 27px; font-family: Arial, sans-serif; font-size: 11px; color: var(--white); text-decoration: underline; }

  .service { position: absolute; top: 705px; width: 200px; }
  .service h3 { font-size: 27px; font-weight: 400; line-height: 28px; color: var(--blue); text-transform: uppercase; }
  .service p { margin-top: 3px; font-family: Arial, sans-serif; font-size: 12px; line-height: 14.5px; color: var(--ink-soft); }
  .service--local { left: 162px; }
  .service--national { left: 434px; }
  .service--ecommerce { left: 707px; }

  .growth-illustration { position: absolute; left: 257px; top: 866px; width: 601px; height: 276px;
    background: linear-gradient(120deg, #ffffff 0%, #eef4fa 45%, #e9e4de 100%); }

  .site-footer { position: absolute; left: 0; top: 1148px; width: 1029px; text-align: center; font-family: Arial, sans-serif; font-size: 12px; color: var(--ink); }
  .footer-nav { display: flex; justify-content: center; gap: 13px; }
  .footer-nav a { color: var(--ink); text-decoration: none; }
  .copyright { margin-top: 2px; }
</style>
</head>
<body>
  <header>
    <div class="brand">
      <span class="brand-mark"></span>
      <span class="brand-name">Marlow Tappers</span>
    </div>
    <div class="phone">Call 1300 48 27 90</div>
    <div class="header-rule"></div>
    <nav class="main-nav">
      <a href="#" class="is-active">Home</a>
      <a href="#">About</a>
      <a href="#">Vexora bidlines</a>
      <a href="#">Other services</a>
      <a href="#">Why choose us?</a>
      <a href="#">Contact</a>
    </nav>
  </header>

  <main>
    <div class="hero-badge">?</div>
    <h1 class="hero-title">Want <span class="muted">more sales and leads</span> from your bidlines campaign without increasing your budget?</h1>

    <section class="health-check">
      <h2>FREE BIDLINES HEALTH CHECK</h2>
      <div class="url-field">http://</div>
      <a href="#" class="next-link">next &gt;&gt;</a>
    </section>

    <section class="service service--local">
      <h3>Local<br>bidlines</h3>
      <p>Lorem ipsum dolor sit amet,<br>consectetur adipiscing elit.<br>Fusce nec dolor mi...</p>
    </section>
    <section class="service service--national">
      <h3>National<br>bidlines</h3>
      <p>Lorem ipsum dolor sit amet,<br>consectetur adipiscing elit.<br>Fusce nec dolor mi...</p>
    </section>
    <section class="service service--ecommerce">
      <h3>Ecommerce<br>bidlines</h3>
      <p>Lorem ipsum dolor sit amet,<br>consectetur adipiscing elit.<br>Fusce nec dolor mi...</p>
    </section>

    <div class="growth-illustration" role="img" aria-label="Hand with a marker sketching a rising bar chart with a blue upward arrow"></div>
  </main>

  <footer class="site-footer">
    <nav class="footer-nav">
      <a href="#">Home</a>
      <a href="#">About</a>
      <a href="#">Vexora bidlines</a>
      <a href="#">Other services</a>
      <a href="#">Why choose us?</a>
      <a href="#">Contact</a>
    </nav>
    <div class="copyright">© 2012 Marlow Tappers</div>
  </footer>
</body>
</html>
```